Drug safety monitoring company requires a new corporate website

We are an outsourcing partner to large and small companies within the pharmaceutical industry. Our current website www.quorvanta.co.uk has not been updated in a long time. We want a new web site that is responsive and modern but with a clearly corporate and professional feel. We want a design based on a 12 column grid system (mobile and desktop version). We want to use a new, modern font (not the standard web fonts) - we will purchase as required. Content can be used as is from the current website. Red and white are the corporate colours, so a palate should be developed to match. We do not need as much red as is in the current website. New icons (preferably in svg format) would be great. We can also purchase new images from Framly (or other) as required. We would prefer submissions in Sketch if possible.

Target Market(s)

Pharmaceutical companies

Number of Pages Required

1 page

Font styles to use
Sans Serif

Colors
ec1f27
ffffff

Requirements
Must have
• Design based on 12 column grid system.
Responsive design (i.e. require a mobile and desktop version).
How should the menu look between desktop and mobile?
A coherent colour palete.
Content to come from the existing website: www.quorvanta.co.uk
How should links be styled?
How should headings, sub-headings, paragraphs be styled?
Nice to have
• Custom developed icons (these are along the bottom of the page on the existing website: Medical Information; Pharmacovigilance; Literature Monitoring; Training).
New imagery (the images on the current website are dated).
Submission ideally as Sketch files (but we are okay with photoshop too).
A new, modern, non-standard font.
Not so much red in the design.
If we had buttons on the website, how should they be styled?
If we had a form on the website, how should the fields be styled?

```html
<!DOCTYPE html>
<html lang="en">
<head>
<meta charset="utf-8">
<title>Quorvanta Pharmacovigilance</title>
<link href="https://fonts.googleapis.com/css2?family=Alegreya+Sans:wght@300;400;500;700&family=Roboto:wght@400;500&display=swap" rel="stylesheet">
<style>
:root{
  --red:#ec1f27;
  --ink:#1f1f1f;
  --dark:#222222;
  --text:#6d6d6d;
  --soft:#f3f3f3;
  --line:#dddddd;
  --white:#ffffff;
}
*{box-sizing:border-box;margin:0;padding:0}
html,body{width:1200px;height:2738px;overflow:hidden}
body{font-family:"Alegreya Sans",sans-serif;color:var(--ink);background:var(--white);position:relative}
a{color:inherit;text-decoration:none}
.abs{position:absolute}
.btn{display:inline-flex;align-items:center;gap:8px;border-radius:20px;font-size:13px;font-weight:500;font-family:"Roboto",sans-serif;height:34px;padding:0 18px;white-space:nowrap}
.btn svg{width:16px;height:10px}
.btn-red{background:var(--red);color:var(--white)}
.btn-dark{background:var(--ink);color:var(--white)}
.btn-outline{border:1px solid var(--red);color:var(--red);font-weight:400;font-size:11px}

/* top bar */
.topbar{top:0;left:0;width:1200px;height:37px;background:var(--ink);color:#e6e6e6;font-size:11px}
.topbar .info{left:161px;top:11px;display:flex;gap:14px}
.topbar .info span{display:flex;align-items:center;gap:5px}
.topbar .social{right:162px;top:12px;display:flex;gap:14px}
.dot{width:12px;height:12px;border-radius:50%;background:#e6e6e6;display:block}

/* header */
.header{top:37px;left:0;width:1200px;height:87px;background:var(--white);border-bottom:2px solid var(--red)}
.brand{left:162px;top:27px;display:flex;align-items:center;gap:10px}
.brand .mark{width:26px;height:26px;border-radius:50%;background:var(--red);display:block}
.brand .name{font-size:26px;font-weight:500;color:var(--ink);line-height:30px}
.nav{left:428px;top:40px;display:flex;gap:19px;font-size:12px;font-weight:700;color:var(--ink)}
.callbox{left:882px;top:28px;display:flex;align-items:center;gap:16px;border-left:1px dashed #999;padding-left:18px;height:36px}
.callbox strong{display:block;font-size:15px;font-weight:500;font-family:"Roboto",sans-serif}
.callbox small{font-size:11px;color:#555}

/* hero */
.hero{top:124px;left:0;width:1200px;height:526px;background:linear-gradient(120deg,#3a3530 0%,#1e1c1a 45%,#2b2622 70%,#4a4038 100%)}
.arrow-btn{top:239px;width:34px;height:34px;border-radius:50%;background:var(--white);display:flex;align-items:center;justify-content:center}
.hero-card{left:284px;top:128px;width:633px;height:270px;display:flex}
.hero-main{width:445px;background:var(--white);padding:30px 14px 0 20px}
.hero-main h1{font-size:24px;font-weight:500;line-height:33px;color:var(--ink)}
.hero-main p{font-size:12.5px;color:var(--text);font-weight:300;line-height:20px;margin:10px 0 16px}
.hero-main .btns{display:flex;gap:14px}
.hero-side{width:188px;background:var(--soft);text-align:center;padding-top:48px}
.hero-side p{color:var(--red);font-size:11.5px;line-height:16px;margin:20px 14px 24px}

/* welcome */
.welcome{top:650px;left:0;width:1200px;height:641px;background:var(--soft);overflow:hidden}
.welcome .blob{left:-180px;top:-40px;width:840px;height:740px;border-radius:48% 52% 45% 55%;background:#ececec}
.welcome-text{left:162px;top:74px;width:480px}
.welcome-text h2{font-size:28px;font-weight:500;line-height:34px;margin-bottom:22px}
.welcome-text p{font-size:11.5px;color:var(--text);font-weight:300;line-height:18px;margin-bottom:18px}
.welcome-photo{left:691px;top:110px;width:348px;height:375px;border-radius:4px;background:linear-gradient(160deg,#4cbfa6 0%,#39a990 55%,#b9c0c7 80%,#9fa7ae 100%)}

/* services */
.services{top:1291px;left:0;width:1200px;height:457px;background:var(--white)}
.services h2{top:72px;left:0;width:1200px;text-align:center;font-size:27px;font-weight:500}
.cards{left:162px;top:144px;display:flex;gap:31px}
.card{width:196px;height:232px;border:1px solid var(--line);text-align:center;padding-top:20px;position:relative}
.card h3{font-size:18px;font-weight:500;margin:8px 0 10px}
.card p{font-size:11.5px;color:var(--text);font-weight:300;line-height:16px;padding:0 22px}
.card .foot{position:absolute;left:20px;right:20px;bottom:20px;display:flex;align-items:center;gap:10px}
.card .foot i{flex:1;height:1px;background:var(--line)}
.card .btn{height:30px;font-size:11px;padding:0 14px}

/* consultation */
.consult{top:1748px;left:0;width:1200px;height:540px;background:linear-gradient(100deg,#ef8c8e 0%,#f08f8f 55%,#ec9a98 80%,#e8a9a6 100%)}
.consult-text{left:160px;top:168px;width:430px;text-align:center}
.consult-text h2{font-size:31px;font-weight:500;line-height:36px;color:#2b1416}
.consult-text .call{margin:14px 0 22px;color:var(--white);font-size:13px;font-weight:700}
.consult-text .call b{font-size:20px;color:#2b1416;font-weight:500;margin-left:6px}
.form-box{left:615px;top:44px;width:424px;height:450px;background:var(--white);padding:26px 29px}
.form-box .kicker{font-size:15px;color:var(--ink)}
.form-box h3{font-size:26px;font-weight:500;margin:6px 0 16px}
.field{height:39px;border:1px solid #d6d6d6;border-radius:20px;margin-bottom:14px;padding:0 19px;display:flex;align-items:center;font-size:11.5px;color:#888}
.field.area{height:90px;align-items:flex-start;padding-top:14px}
.form-box .btn{position:absolute;right:29px;bottom:38px;font-size:11px;height:36px}

/* footer */
.footer{top:2288px;left:0;width:1200px;height:400px;background:var(--dark);color:#d0d0d0}
.contact-row{left:162px;top:34px;width:877px;display:flex;align-items:center}
.ci{display:flex;gap:12px;align-items:flex-start}
.ci h4{color:var(--white);font-size:14px;font-weight:500;margin-bottom:6px}
.ci p{font-size:10.5px;line-height:15px;color:#bbb}
.footer .rule{left:162px;top:126px;width:877px;height:1px;background:#555}
.fcol h5{color:var(--white);font-size:13px;font-weight:700;margin-bottom:16px}
.fcol p,.fcol a{font-size:11px;line-height:18px;color:#bbb}
.links{display:grid;grid-template-columns:144px 100px;row-gap:7px;font-size:10.5px}
.subscribe{display:flex;margin-top:16px;height:38px;border-radius:20px;overflow:hidden;width:348px}
.subscribe span{flex:1;background:var(--white);color:#888;font-size:10.5px;padding-left:18px;display:flex;align-items:center}
.subscribe b{width:101px;background:var(--red);color:var(--white);font-weight:400;font-size:11px;display:flex;align-items:center;justify-content:center}
.socials{display:flex;gap:4px;margin-top:22px}
.socials i{width:29px;height:29px;border-radius:50%;background:var(--red);display:block}
.copy{top:2688px;left:0;width:1200px;height:50px;background:var(--red);color:var(--white);font-size:10px;text-align:center;line-height:50px}
</style>
</head>
<body>

<div class="abs topbar">
  <div class="abs info">
    <span><svg width="10" height="8" viewBox="0 0 10 8"><rect x=".5" y=".5" width="9" height="7" fill="none" stroke="#ddd"/><path d="M.5 .5 5 4.5 9.5.5" fill="none" stroke="#ddd"/></svg>info@example.com</span>
    <span><svg width="9" height="11" viewBox="0 0 9 11"><path d="M4.5 0a4.5 4.5 0 0 0-4.5 4.5C0 8 4.5 11 4.5 11S9 8 9 4.5A4.5 4.5 0 0 0 4.5 0z" fill="#ddd"/><circle cx="4.5" cy="4.5" r="1.6" fill="#1f1f1f"/></svg>England &amp; Wales : 04418273</span>
  </div>
  <div class="abs social"><i class="dot"></i><i class="dot"></i><i class="dot"></i><i class="dot"></i></div>
</div>

<header class="abs header">
  <a class="abs brand" href="#"><span class="mark"></span><span class="name">Quorvanta</span></a>
  <nav class="abs nav"><a href="#">Home</a><a href="#">About Us</a><a href="#">QPPV</a><a href="#">Our Services ⌄</a><a href="#">Contact Us</a><a href="#">Client</a></nav>
  <div class="abs callbox">
    <svg width="28" height="28" viewBox="0 0 24 24"><path d="M6.6 10.8a15.1 15.1 0 0 0 6.6 6.6l2.2-2.2a1 1 0 0 1 1-.25 11.4 11.4 0 0 0 3.6.57 1 1 0 0 1 1 1V20a1 1 0 0 1-1 1A17 17 0 0 1 3 4a1 1 0 0 1 1-1h3.5a1 1 0 0 1 1 1c0 1.25.2 2.45.57 3.57a1 1 0 0 1-.25 1z" fill="#1f1f1f"/></svg>
    <div><strong>0330 555 0142</strong><small>Need Help, Make a Call</small></div>
  </div>
</header>

<section class="abs hero" role="img" aria-label="Dark photograph of a worker in protective gloves">
  <span class="abs arrow-btn" style="left:34px"><svg width="18" height="12" viewBox="0 0 18 12"><path d="M17 6H1M6 1 1 6l5 5" fill="none" stroke="#1f1f1f" stroke-width="1.4"/></svg></span>
  <span class="abs arrow-btn" style="left:1129px"><svg width="18" height="12" viewBox="0 0 18 12"><path d="M1 6h16M12 1l5 5-5 5" fill="none" stroke="#1f1f1f" stroke-width="1.4"/></svg></span>
  <div class="abs hero-card">
    <div class="hero-main">
      <h1>At Quorvanta we ensure that your business has the best Pharmacovigilance support in the industry</h1>
      <p>Lorem ipsum dolor sit amet, consectetur adipiscing elit. Nulla eu velit nibh. Praesent rutrum, dui quis semper. Lorem ipsum dolor sit amet, consectetur adipiscing elit.</p>
      <div class="btns">
        <a class="btn btn-red" href="#">Contact Us <svg viewBox="0 0 16 10"><path d="M0 5h15M11 1l4 4-4 4" fill="none" stroke="#fff" stroke-width="1.3"/></svg></a>
        <a class="btn btn-outline" href="#">Our Services <svg viewBox="0 0 16 10"><path d="M0 5h15M11 1l4 4-4 4" fill="none" stroke="#ec1f27" stroke-width="1.3"/></svg></a>
      </div>
    </div>
    <div class="hero-side">
      <svg width="76" height="74" viewBox="0 0 76 74" fill="none" stroke="#1f1f1f" stroke-width="2"><rect x="14" y="10" width="42" height="58" rx="3"/><rect x="26" y="5" width="18" height="9" rx="2"/><path d="M5 40h12l5-10 6 18 5-12h10"/><path d="M56 8l12 4v10c0 8-6 12-12 14-6-2-12-6-12-14V12z"/><path d="M56 16v12M50 22h12"/><path d="M24 58h10M40 56l5 5 9-10"/></svg>
      <p>Lorem ipsum dolor sit amet, consectetur adipiscing elit.</p>
      <a class="btn btn-dark" href="#">Read More <svg viewBox="0 0 16 10"><path d="M0 5h15M11 1l4 4-4 4" fill="none" stroke="#fff" stroke-width="1.3"/></svg></a>
    </div>
  </div>
</section>

<section class="abs welcome">
  <div class="abs blob"></div>
  <div class="abs welcome-text">
    <h2>Welcome to the Quorvanta Pharmacovigilance</h2>
    <p>We are an outsourcing partner to large and small companies within the pharmaceutical industry. Our range of services is tailored to suit each of our client’s needs and cover both human and veterinary medicinal products.</p>
    <p>Pharmacovigilance is defined by WHO as ‘The science and activities relating to the detection, assessment, understanding and prevention of adverse effects or any other drug-related problems’. The process is one of managing risk associated with medicinal products, in an effort to promote their safe and effective use by prescribers and patients.</p>
    <p>Our primary functions are EU QPPV and related pharmacovigilance services to assist and support Marketing Authorisation Holders (MAH), of pharmaceutical product licences, in their efforts to remain compliant with EU regulatory requirements (Regulation 1235/2010 and Directive 2010/84/EU) the deadline for which implementing ended on 21 July 2012.</p>
    <p>The regulatory environment is an ever-changing and evolving one. Legislation is global and the management of this process is complex, requiring a strong relationship between Marketing Authorisation Holders and their QPPV.</p>
    <p>Good Pharmacovigilance Practice is dependant on a sound understanding of the key principles of this science and the ability to apply this knowledge competently on behalf of the client.</p>
    <a class="btn btn-dark" href="#" style="margin-top:14px">About Us <svg viewBox="0 0 16 10"><path d="M0 5h15M11 1l4 4-4 4" fill="none" stroke="#fff" stroke-width="1.3"/></svg></a>
  </div>
  <div class="abs welcome-photo" role="img" aria-label="Gloved hands holding a handful of tablets in front of green scrubs"></div>
</section>

<section class="abs services">
  <h2 class="abs">Our Services</h2>
  <div class="abs cards">
    <div class="card">
      <svg width="48" height="48" viewBox="0 0 48 48" fill="none" stroke="#ec1f27" stroke-width="2"><rect x="4" y="3" width="40" height="26"/><circle cx="24" cy="16" r="8"/><path d="M24 11v10M19 16h10"/><rect x="6" y="33" width="10" height="8"/><rect x="19" y="33" width="10" height="8"/><rect x="32" y="33" width="10" height="8"/><path d="M4 45h40"/></svg>
      <h3>Medical Information</h3>
      <p>Professional enquiry handling to support the safe and effective use of your products.</p>
      <div class="foot"><i></i><a class="btn btn-dark" href="#">Read More <svg viewBox="0 0 16 10"><path d="M0 5h15M11 1l4 4-4 4" fill="none" stroke="#fff" stroke-width="1.3"/></svg></a><i></i></div>
    </div>
    <div class="card">
      <svg width="48" height="48" viewBox="0 0 48 48" fill="none" stroke="#ec1f27" stroke-width="2.2"><path d="M24 42C10 32 4 25 4 16a10 10 0 0 1 20-3 10 10 0 0 1 20 3c0 9-6 16-20 26z"/><path d="M8 24h10l3-6 5 12 4-8 3 2h7"/></svg>
      <h3>Pharmacovigilance</h3>
      <p>Ease the regulatory burden and keep compliant with current pharmacovigilance legislation.</p>
      <div class="foot"><i></i><a class="btn btn-dark" href="#">Read More <svg viewBox="0 0 16 10"><path d="M0 5h15M11 1l4 4-4 4" fill="none" stroke="#fff" stroke-width="1.3"/></svg></a><i></i></div>
    </div>
    <div class="card">
      <svg width="48" height="48" viewBox="0 0 48 48" fill="none" stroke="#ec1f27" stroke-width="2"><path d="M4 8h17a3 3 0 0 1 3 3v28a3 3 0 0 0-3-3H4zM44 8H27a3 3 0 0 0-3 3v28a3 3 0 0 1 3-3h17z"/><path d="M9 15h10M9 20h10M9 25h10M29 15h10M29 20h10M29 25h10"/><path d="M2 42h44"/></svg>
      <h3>Literature Monitoring</h3>
      <p>Product safety through surveillance of published articles and case reports.</p>
      <div class="foot"><i></i><a class="btn btn-dark" href="#">Read More <svg viewBox="0 0 16 10"><path d="M0 5h15M11 1l4 4-4 4" fill="none" stroke="#fff" stroke-width="1.3"/></svg></a><i></i></div>
    </div>
    <div class="card">
      <svg width="48" height="48" viewBox="0 0 48 48" fill="none" stroke="#ec1f27" stroke-width="2"><rect x="3" y="6" width="42" height="34" rx="2"/><circle cx="16" cy="19" r="5"/><path d="M8 34a8 8 0 0 1 16 0z"/><path d="M29 16h11M29 22h11M29 28h11"/></svg>
      <h3>Training</h3>
      <p>Confident staff to support the pharmacovigilance process.</p>
      <div class="foot"><i></i><a class="btn btn-dark" href="#">Read More <svg viewBox="0 0 16 10"><path d="M0 5h15M11 1l4 4-4 4" fill="none" stroke="#fff" stroke-width="1.3"/></svg></a><i></i></div>
    </div>
  </div>
</section>

<section class="abs consult" role="img" aria-label="Soft red tinted photograph of a doctor with a stethoscope">
  <div class="abs consult-text">
    <h2>Free consultation and assessment of your business requirements.</h2>
    <p class="call">Get Your Quote or Call: <b>0330 555 0142</b></p>
    <a class="btn btn-dark" href="#">Contact Us <svg viewBox="0 0 16 10"><path d="M0 5h15M11 1l4 4-4 4" fill="none" stroke="#fff" stroke-width="1.3"/></svg></a>
  </div>
  <form class="abs form-box">
    <p class="kicker">Fill Form</p>
    <h3>Free Consultation</h3>
    <div class="field">Your Name</div>
    <div class="field">Your Email *</div>
    <div class="field">Your Phone</div>
    <div class="field area">Your message</div>
    <a class="btn btn-red" href="#">Send Message <svg viewBox="0 0 16 10"><path d="M0 5h15M11 1l4 4-4 4" fill="none" stroke="#fff" stroke-width="1.3"/></svg></a>
  </form>
</section>

<footer class="abs footer">
  <div class="abs contact-row">
    <div class="ci" style="width:241px">
      <svg width="54" height="54" viewBox="0 0 54 54" fill="none" stroke="#ec1f27" stroke-width="2"><path d="M27 4a12 12 0 0 0-12 12c0 10 12 24 12 24s12-14 12-24A12 12 0 0 0 27 4z"/><circle cx="27" cy="16" r="5"/><path d="M14 34 3 50h48L40 34"/></svg>
      <div><h4>Address</h4><p>Lorem ipsum dolor sit amet,<br>consectetur</p></div>
    </div>
    <div class="ci" style="width:233px">
      <svg width="54" height="54" viewBox="0 0 54 54" fill="none" stroke="#ec1f27" stroke-width="2"><path d="M4 18c4-8 42-8 46 0l-3 6-9-2v-6H16v6l-9 2z"/><path d="M10 28h34l6 20H4z"/><text x="17" y="44" font-size="12" fill="#ec1f27" stroke="none" font-family="Arial,sans-serif" font-weight="700">24</text></svg>
      <div><h4>Contact Info</h4><p>0330 555 0142<br>+1 123 4567 890</p></div>
    </div>
    <div class="ci" style="width:280px">
      <svg width="54" height="54" viewBox="0 0 54 54" fill="none" stroke="#ec1f27" stroke-width="2"><path d="M3 22v28h48V22L27 6z"/><path d="M3 22l24 16 24-16M3 50l18-14M51 50 33 36"/><path d="M15 28V14h24v14M20 19h14M20 24h14"/></svg>
      <div><h4>Email Address</h4><p>info@example.com<br>info@example.com</p></div>
    </div>
    <a class="btn btn-red" href="#" style="margin-left:auto;width:123px;justify-content:center;font-size:12px">Get in Touch</a>
  </div>
  <div class="abs rule"></div>
  <div class="abs fcol" style="left:162px;top:184px;width:205px">
    <h5>ABOUT US</h5>
    <p>Quorvanta Pharmacovigilance operates from offices in Harbour Court, Westfield situated in Ashbridge. We are an outsourcing provider of medical information enquiry handling services and pharmacovigilance services to various clients within the pharmaceutical industry.</p>
  </div>
  <div class="abs fcol" style="left:411px;top:184px">
    <h5>COMPANY</h5>
    <div class="links"><a href="#">Home</a><a href="#">About Us</a><a href="#">QPPV</a><a href="#">Services</a><a href="#">Contact Us</a><a href="#">Client</a></div>
  </div>
  <div class="abs fcol" style="left:691px;top:184px">
    <h5>SUBSCRIBE OUR NEWSLETTER</h5>
    <p style="font-size:10.5px;line-height:22px">Weekly Breaking News Analysis And Cutting Edge<br>Advices On Job Searching.</p>
    <div class="subscribe"><span>Email Address</span><b>SUBSCRIBE</b></div>
    <div class="socials"><i></i><i></i><i></i><i></i></div>
  </div>
</footer>

<div class="abs copy">Copyright © 2020. All Rights Reserved.</div>

</body>
</html>
```